Need a new design for Glass Cleaner label. The brand name already exists i.e. BRIXO. Pell is the company name. Looking for new design. It's application is for cleaning glasses in houses, cars, offices e.t.c. Our product gives streak free shine and anti static effect. Images of old label design is attached. Bottle will be same as before. It's better to show a car as well in the design but not necessary. New logo's of brixo can also be designed.

Target Market(s)

Household and automobile

Industry/Entity Type

It Company

```html
<!DOCTYPE html>
<html lang="en">
<head>
<meta charset="utf-8">
<title>BRIXO Glass Cleaner Label</title>
<link rel="stylesheet" href="https://fonts.googleapis.com/css2?family=Oswald:wght@500;600;700&family=Rubik:wght@800&display=swap">
<style>
  :root {
    --label-red: #ec1c24;
    --label-yellow: #fff200;
    --label-navy: #17244f;
    --tag-yellow: #ffeb00;
    --ink: #111111;
    --paper: #ffffff;
    --mist: #dbe9f2;
  }
  html, body {
    margin: 0;
    padding: 0;
    width: 997px;
    height: 1200px;
    overflow: hidden;
    background: var(--paper);
  }
  .label-canvas {
    display: block;
    width: 997px;
    height: 1200px;
  }
  .brand-mark {
    font-family: "Oswald", sans-serif;
    font-weight: 700;
    fill: var(--paper);
  }
  .product-name {
    font-family: "Rubik", sans-serif;
    font-weight: 800;
    fill: var(--label-red);
    stroke: var(--paper);
    stroke-width: 4px;
    paint-order: stroke;
  }
  .claim-tag-text {
    font-family: "Oswald", sans-serif;
    font-weight: 600;
    fill: var(--paper);
  }
  .burst-text {
    font-family: "Oswald", sans-serif;
    font-weight: 600;
    fill: var(--ink);
  }
  .maker-name {
    font-family: "Oswald", sans-serif;
    font-weight: 600;
    fill: var(--tag-yellow);
  }
</style>
</head>
<body>
<svg class="label-canvas" viewBox="0 0 997 1200" xmlns="http://www.w3.org/2000/svg">
  <defs>
    <clipPath id="label-shape">
      <path d="M690 95 Q765 82 782 150 L800 320 Q812 700 802 920 Q792 1070 680 1112 Q520 1126 380 1112 Q236 1092 228 960 L228 560 Q230 490 300 445 L640 128 Q662 100 690 95 Z"/>
    </clipPath>
    <linearGradient id="body-tone" x1="0" y1="0" x2="1" y2="0">
      <stop offset="0" stop-color="#cfe1ee"/>
      <stop offset="0.25" stop-color="#f4f8fb"/>
      <stop offset="0.75" stop-color="#f7fafc"/>
      <stop offset="1" stop-color="#d9e7f1"/>
    </linearGradient>
    <linearGradient id="scene-tone" x1="0" y1="0" x2="0.3" y2="1">
      <stop offset="0" stop-color="#f4f8fb" stop-opacity="0"/>
      <stop offset="0.12" stop-color="#c9d3d6"/>
      <stop offset="0.32" stop-color="#7f8f86"/>
      <stop offset="0.5" stop-color="#5e8ea8"/>
      <stop offset="0.72" stop-color="#3a8fca"/>
      <stop offset="1" stop-color="#8ccbec"/>
    </linearGradient>
    <radialGradient id="scene-glow" cx="0.72" cy="0.35" r="0.45">
      <stop offset="0" stop-color="#2f6fc2" stop-opacity="0.55"/>
      <stop offset="1" stop-color="#2f6fc2" stop-opacity="0"/>
    </radialGradient>
  </defs>

  <g class="label" clip-path="url(#label-shape)">
    <rect class="label-base" x="200" y="80" width="640" height="1060" fill="url(#body-tone)"/>

    <g class="scene-photo" role="img" aria-label="Hand spraying blue glass cleaner onto a car windscreen and wiping it with a cloth">
      <rect x="200" y="520" width="640" height="500" fill="url(#scene-tone)"/>
      <rect x="200" y="520" width="640" height="500" fill="url(#scene-glow)"/>
    </g>

    <path class="top-band-yellow" d="M200 476 Q500 400 840 418 L840 440 Q500 420 200 500 Z" fill="var(--label-yellow)"/>
    <path class="top-band-red" d="M200 80 L840 80 L840 418 Q500 400 200 476 Z" fill="var(--label-red)"/>

    <path class="bottom-band" d="M200 1000 Q520 960 840 990 L840 1140 L200 1140 Z" fill="var(--label-navy)"/>
  </g>

  <text class="brand-mark" x="680" y="340" text-anchor="middle" font-size="120">Pell</text>

  <text class="product-name" x="345" y="612" font-size="140" textLength="425" lengthAdjust="spacingAndGlyphs" transform="rotate(-3 560 560)">BRIXO</text>

  <g class="claim-tag" transform="rotate(-5 370 690)">
    <rect x="228" y="662" width="290" height="60" fill="var(--label-red)"/>
    <text class="claim-tag-text" x="388" y="705" text-anchor="middle" font-size="34">Anti Static Effect</text>
  </g>

  <g class="claim-burst" transform="translate(740 652)">
    <polygon fill="var(--tag-yellow)" stroke="var(--label-red)" stroke-width="3"
      points="72,0 61.3,9.7 68.5,22.2 55.2,28.1 58.2,42.3 43.8,43.8 42.3,58.2 28.1,55.2 22.2,68.5 9.7,61.3 0,72 -9.7,61.3 -22.2,68.5 -28.1,55.2 -42.3,58.2 -43.8,43.8 -58.2,42.3 -55.2,28.1 -68.5,22.2 -61.3,9.7 -72,0 -61.3,-9.7 -68.5,-22.2 -55.2,-28.1 -58.2,-42.3 -43.8,-43.8 -42.3,-58.2 -28.1,-55.2 -22.2,-68.5 -9.7,-61.3 0,-72 9.7,-61.3 22.2,-68.5 28.1,-55.2 42.3,-58.2 43.8,-43.8 58.2,-42.3 55.2,-28.1 68.5,-22.2 61.3,-9.7"/>
    <text class="burst-text" text-anchor="middle" font-size="29">
      <tspan x="-6" y="-18">Streak</tspan>
      <tspan x="-4" y="12">Free</tspan>
      <tspan x="-2" y="42">Shine</tspan>
    </text>
  </g>

  <text class="maker-name" x="525" y="1092" text-anchor="middle" font-size="30">Pell Chemical Company</text>
</svg>
</body>
</html>
```